Packaging Design job - Product : Supplement for Travel Sickness

We need a packaging design for a travel sickness supplement called "VOLUMAR"

VOLUMAR It is a dietary supplement based on ginger which has properties fighting against motion sickness.

Ginger is a root used for many years for its beneficial effects on health. In addition to its stimulating and toning properties which help to resist fatigue, ginger is used as an adjuvant in case of nausea, vomiting and motion sickness. Ideal for pregnant women to combat certain disadvantages of pregnancy.

This product will be in blister form of 30 capsules. We need for this a packaging design for the box.Dimensions: 100 * 20 * 200 mm

We would like to see clean, modern and fresh designs.This should give the impression of professional products of pharmaceutical quality. You will also find attached the logo of our company.Ps : You can change the color of the logo

Mention to put on the box :

• Produit en France: Laboratoire KRANIVO, 24 Rue des Lavandières 37410 BRÉCHAL
• Distribué au Maroc: LUMORAXIN 14 rue Oumaima Tazrouti 30050 FEZ MAROC
• Complément alimentaire, ce n'est pas un médicament
• Voie orale
• Tenir hors de portée des enfants
• Respectez la dose recommandée
• Ce produit ne remplace pas une alimentation variée

Mode d'utilisation (How to use) :

2 à 3 gélules 30 min avant de prendre le véhicule de transport
1 gélule par jour en cas de cure

Font styles to use
Serif
Sans Serif
Script

Requirements
Should not have
• Sales and other "must buy" "guaranteed" etc

```html
<!DOCTYPE html>
<html lang="en">
<head>
<meta charset="utf-8">
<title>VOLUMAR – Box Front</title>
<link rel="stylesheet" href="https://fonts.googleapis.com/css2?family=Poppins:wght@500;700&family=Mulish:wght@400;500&display=swap">
<style>
  :root {
    --bg: #e4e4e4;
    --yellow: #f0e75a;
    --yellow-soft: #f4ec86;
    --white: #ffffff;
    --ink: #231f20;
    --red: #c8202b;
  }
  * { margin: 0; padding: 0; box-sizing: border-box; }
  html, body {
    width: 1200px; height: 1200px; overflow: hidden;
    background: var(--bg);
  }
  .canvas { position: relative; width: 1200px; height: 1200px; }

  .box-front {
    position: absolute; left: 259px; top: 135px;
    width: 498px; height: 997px;
    background: var(--white);
    overflow: hidden;
  }

  .hero-band {
    position: absolute; left: 0; top: 0;
    width: 100%; height: 745px;
    background: var(--yellow);
  }

  .ginger-illustration {
    position: absolute; left: 68px; top: 40px;
    width: 360px; height: 660px;
  }

  .product-name {
    position: absolute; left: 196px; top: 52px;
    writing-mode: vertical-rl;
    font-family: "Poppins", sans-serif;
    font-weight: 500;
    font-size: 142px;
    line-height: 1;
    letter-spacing: -2px;
    color: var(--ink);
  }

  .brand {
    position: absolute; left: 418px; top: 58px;
    display: flex; flex-direction: column; align-items: center; gap: 8px;
  }
  .brand-mark {
    width: 14px; height: 14px; border-radius: 50%;
    background: var(--red);
  }
  .brand-name {
    writing-mode: vertical-rl;
    font-family: "Poppins", sans-serif;
    font-weight: 700;
    font-size: 27px;
    line-height: 1;
    color: var(--ink);
  }

  .info-panel {
    position: absolute; left: 0; top: 745px;
    width: 100%; height: 252px;
    text-align: center;
    font-family: "Mulish", sans-serif;
    color: var(--ink);
  }
  .info-panel .category {
    position: absolute; left: 0; right: 0; top: 44px;
    font-size: 33px; font-weight: 400; letter-spacing: 0.2px;
  }
  .info-panel .rule {
    position: absolute; left: 68px; width: 359px; height: 1.5px;
    background: var(--ink);
  }
  .info-panel .rule-top { top: 86px; }
  .info-panel .rule-bottom { top: 150px; }
  .info-panel .base {
    position: absolute; left: 0; right: 0; top: 96px;
    font-size: 35px; font-weight: 500;
  }
  .info-panel .count {
    position: absolute; left: 0; right: 0; top: 160px;
    font-size: 22px; letter-spacing: 0.5px;
  }
  .info-panel .count-number {
    color: var(--red); font-size: 38px; margin-right: 10px;
  }
</style>
</head>
<body>
<div class="canvas">
  <div class="box-front">
    <div class="hero-band">
      <svg class="ginger-illustration" viewBox="0 0 360 660" role="img" aria-label="Faint line illustration of a ginger root">
        <path d="M150 20 C230 0 300 60 290 160 C340 260 380 380 320 470 C300 560 230 650 140 640 C60 630 40 540 70 460 C10 380 0 300 60 250 C40 160 80 50 150 20 Z" fill="var(--yellow-soft)" opacity="0.7"/>
      </svg>
      <div class="product-name">VOLUMAR</div>
      <div class="brand">
        <span class="brand-mark"></span>
        <span class="brand-name">LUMORAXIN</span>
      </div>
    </div>
    <div class="info-panel">
      <p class="category">DIETARY SUPPLEMENT</p>
      <span class="rule rule-top"></span>
      <p class="base">based on ginger</p>
      <span class="rule rule-bottom"></span>
      <p class="count"><span class="count-number">30</span>CAPSULES</p>
    </div>
  </div>
</div>
</body>
</html>
```